Innovative three sided toothbrush packaging design

Engineered with innovation in mind, this toothbrush features a groundbreaking three-sided design that revolutionises the brushing experience for users of all ages..

Creating an innovative packaging design for a three-sided toothbrush that appeals to both children and adults while standing out on a supermarket shelf requires a balance of creativity, functionality, and premium aesthetics.
- Soft bristle
- DENTISTS RECOMMEND
BRUSHING AT LEAST TWICE A DAY
REPLACING YOUR TOOTHBRUSH EVERY 3 MONTHS
CLEANING YOUR TONGUE TO REMOVE BACTERIA

- NZ OWNED
MANUFACTURED IN CHINA

Company name: Pipsy Grins NZ

Social media:
Join us on social!
Chatterbox logo & snapgrove logo

Questions, comments or ideas?
admin@pipsygrinsnz.example
www.pipsygrinsnz.example

BRISTLE MATERIAL- Varkell filament - a high-quality nylon thread, strong and wear-resistant

HANDLE MATERIAL- PP + TPE

Suitable for sensitive teeth and gums

Target Market(s)

Everyone!

Industry/Entity Type

Oral Health Care / dental

Font styles to use
Sans Serif

Colors

Designer to choose colors to be used in the design.

Requirements
Must have
• Toothbrush head to be visible through packaging OR picture of toothbrush head on packaging (this is not a standard toothbrush so our point of difference must be highlighted)
Nice to have
• Packaging that suits the full colour range we have on offer. Or a standard design that we can make a slight adjustment to allowing for different colour options.
Should not have
• No red or blue (competitor colours and will not stand out on the shelfs)

```html
<!DOCTYPE html>
<html lang="en">
<head>
<meta charset="utf-8">
<title>Pipsy Grins – Toothbrush Pack Front</title>
<link rel="stylesheet" href="https://fonts.googleapis.com/css2?family=Anton&family=Poppins:wght@300;500&family=Oswald:wght@700&display=swap">
<style>
  :root {
    --plum-deep: #3d1653;
    --plum: #4f2a7a;
    --violet: #6a4ea4;
    --lavender: #8f82c0;
    --teal-soft: #5fa9c7;
    --magenta: #c95aa9;
    --cream: #f7f1bd;
    --ink: #383536;
    --white: #ffffff;
    --window-top: #b3a4c2;
    --window-bottom: #7a6688;
  }
  * { margin: 0; padding: 0; box-sizing: border-box; }
  html, body { width: 1200px; height: 4814px; overflow: hidden; }
  body { background: var(--plum-deep); }

  .pack-front {
    position: relative;
    width: 1200px;
    height: 4814px;
    overflow: hidden;
    background:
      radial-gradient(ellipse 900px 1300px at 100% 82%, rgba(201,90,169,0.95), rgba(201,90,169,0) 70%),
      radial-gradient(ellipse 800px 1200px at 0% 100%, rgba(95,169,199,0.95), rgba(95,169,199,0) 70%),
      radial-gradient(ellipse 700px 900px at 0% 52%, rgba(143,130,192,0.7), rgba(143,130,192,0) 70%),
      linear-gradient(180deg, var(--plum-deep) 0%, var(--plum) 25%, var(--violet) 50%, var(--lavender) 75%, #a77ab8 100%);
  }

  .bubble {
    position: absolute;
    border-radius: 50%;
    background: rgba(255,255,255,0.08);
    border: 2px solid rgba(255,255,255,0.12);
  }
  .bubble--a { left: -180px; top: 2340px; width: 1220px; height: 1100px; }
  .bubble--b { left: 655px;  top: 2090px; width: 540px;  height: 540px; }
  .bubble--c { left: 130px;  top: 1735px; width: 420px;  height: 420px; }
  .bubble--d { left: 925px;  top: 3720px; width: 340px;  height: 340px; }

  .brush-window {
    position: absolute;
    left: 159px;
    top: 346px;
    width: 882px;
    height: 1140px;
    border-radius: 300px 300px 160px 160px;
    background: linear-gradient(160deg, var(--window-top) 0%, var(--window-bottom) 100%);
    opacity: 0.85;
  }

  .brand-badge {
    position: absolute;
    left: 305px;
    top: 1617px;
    width: 602px;
    height: 602px;
    border-radius: 50%;
    background: var(--cream);
    display: flex;
    align-items: center;
    justify-content: center;
    text-align: center;
  }
  .brand-badge__name {
    font-family: "Poppins", sans-serif;
    font-weight: 500;
    font-size: 62px;
    letter-spacing: 6px;
    line-height: 1.25;
    color: var(--ink);
    text-transform: uppercase;
  }

  .brand-name,
  .tagline {
    position: absolute;
    writing-mode: vertical-rl;
    transform: rotate(180deg);
    color: var(--white);
    font-family: "Anton", sans-serif;
    white-space: nowrap;
    line-height: 1;
  }
  .brand-name {
    left: 470px;
    top: 2590px;
    height: 1430px;
    font-size: 300px;
    letter-spacing: -6px;
  }
  .tagline {
    left: 380px;
    top: 3400px;
    height: 620px;
    font-size: 64px;
    letter-spacing: -1px;
  }

  .endorsement {
    position: absolute;
    left: 277px;
    top: 4355px;
    display: flex;
    align-items: center;
    gap: 24px;
  }
  .endorsement__icon { width: 194px; height: 190px; }
  .endorsement__text { color: var(--white); line-height: 1; }
  .endorsement__lead {
    display: block;
    font-family: "Poppins", sans-serif;
    font-weight: 300;
    font-size: 68px;
    letter-spacing: 9px;
  }
  .endorsement__main {
    display: block;
    font-family: "Oswald", sans-serif;
    font-weight: 700;
    font-size: 80px;
    letter-spacing: -1px;
    margin-top: 4px;
  }
</style>
</head>
<body>
  <main class="pack-front">
    <div class="bubble bubble--a"></div>
    <div class="bubble bubble--b"></div>
    <div class="bubble bubble--c"></div>
    <div class="bubble bubble--d"></div>

    <div class="brush-window" role="img" aria-label="Tooth-shaped clear window showing the three-sided toothbrush head"></div>

    <div class="brand-badge">
      <span class="brand-badge__name">Pipsy<br>Grins</span>
    </div>

    <h1 class="brand-name">pipsy grins</h1>
    <p class="tagline">big smiles, little brushes</p>

    <div class="endorsement">
      <svg class="endorsement__icon" viewBox="0 0 194 190" fill="none" stroke="var(--cream)" stroke-width="12" stroke-linecap="round" stroke-linejoin="round" aria-hidden="true">
        <path d="M10 95 H55 L95 35 Q110 10 125 25 L115 70 H165 Q185 75 178 100 L160 170 Q155 180 140 180 H80"/>
        <path d="M25 140 H60"/>
        <path d="M40 178 H62"/>
      </svg>
      <div class="endorsement__text">
        <span class="endorsement__lead">DENTISTS</span>
        <span class="endorsement__main">RECOMMEND</span>
      </div>
    </div>
  </main>
</body>
</html>
```